Home Security Company Business Card

Looking for a eye catching business card that is non traditional and stands out but yet still looks professional. It should include all the pertinent information such as name, title, address, telephone, e-mail, website address should definitely stand out and then finally the logo.

Target Market(s)

Residential and Commercial accounts mostly upscale accounts

Industry/Entity Type

Security

Contact Information for Business Card

Name
Title
Address
Office #
Cell #
E-mail
Website

Font styles to use
Serif
Sans Serif

Requirements
Must have
• Logo, two sided color configuration
Nice to have
• You decide
Should not have
• There really aren't any.

```html
<!DOCTYPE html>
<html lang="en">
<head>
<meta charset="utf-8">
<title>Ironvale Security Systems – Business Card</title>
<link rel="stylesheet" href="https://fonts.googleapis.com/css2?family=PT+Sans:wght@400;700&family=Tinos&display=swap">
<style>
  :root {
    --page-bg: #f1efec;
    --card-bg: #fde9a8;
    --brand-red: #7a1a10;
    --text-dark: #2e2a24;
    --brand-gold: #e0a93a;
    --gold-light: #fbe27a;
    --card-shadow: rgba(60, 40, 20, 0.18);
  }
  * { margin: 0; padding: 0; box-sizing: border-box; }
  html, body {
    width: 1200px;
    height: 900px;
    overflow: hidden;
    background: var(--page-bg);
  }
  .canvas {
    position: relative;
    width: 1200px;
    height: 900px;
  }
  .card {
    position: absolute;
    overflow: hidden;
    background: var(--card-bg);
    box-shadow: 0 4px 14px var(--card-shadow);
  }
  .card--front { left: 238px; top: 62px; width: 556px; height: 342px; }
  .card--back  { left: 457px; top: 518px; width: 560px; height: 344px; }

  .card__decoration {
    position: absolute;
    left: 432px;
    top: 0;
    width: 124px;
    height: 330px;
    background: linear-gradient(90deg, var(--brand-gold) 0%, var(--gold-light) 55%, var(--brand-gold) 85%, var(--brand-red) 100%);
  }

  .contact {
    position: absolute;
    left: 43px;
    top: 66px;
    font-family: "PT Sans", sans-serif;
    color: var(--text-dark);
    font-size: 16px;
    line-height: 20px;
  }
  .contact__name {
    font-size: 19px;
    font-weight: 700;
    color: var(--brand-red);
    line-height: 22px;
  }
  .contact__title { margin-bottom: 18px; }
  .contact__address { margin-bottom: 21px; }
  .contact__list { list-style: none; }
  .contact__item {
    display: flex;
    align-items: center;
    gap: 7px;
    font-size: 16px;
  }
  .contact__icon { width: 11px; height: 11px; fill: var(--brand-red); flex: none; }

  .brand {
    position: absolute;
    left: 116px;
    top: 120px;
    display: flex;
    align-items: center;
    gap: 38px;
    font-family: "Tinos", serif;
    color: var(--brand-red);
  }
  .brand__dot {
    width: 104px;
    height: 104px;
    border-radius: 50%;
    background: var(--brand-gold);
  }
  .brand__name {
    font-size: 31px;
    line-height: 30px;
    letter-spacing: 0.5px;
  }
  .brand__tagline {
    font-size: 16px;
    line-height: 17px;
  }
</style>
</head>
<body>
<main class="canvas">
  <section class="card card--front" aria-label="Business card front">
    <div class="card__decoration" role="img" aria-label="Large gold brand emblem decoration along the right edge"></div>
    <div class="contact">
      <p class="contact__name">Daniel Hartley</p>
      <p class="contact__title">Managing Director</p>
      <p class="contact__address">12345, Address Goes Here<br>Country Name, 123456.</p>
      <ul class="contact__list">
        <li class="contact__item">
          <svg class="contact__icon" viewBox="0 0 12 12" aria-hidden="true"><path d="M1 4c0-2 2-3 5-3s5 1 5 3v1H8V4H4v1H1zM2 6h8l1 5H1z"/></svg>
          044-123 456 789
        </li>
        <li class="contact__item">
          <svg class="contact__icon" viewBox="0 0 12 12" aria-hidden="true"><path d="M3 0h6v12H3zM4 1.5v8h4v-8z"/></svg>
          044-123 456 789
        </li>
        <li class="contact__item">
          <svg class="contact__icon" viewBox="0 0 12 12" aria-hidden="true"><path d="M1 2h10v8H1zM1.5 2.5 6 6.5l4.5-4"/></svg>
          info@ironvale.com
        </li>
        <li class="contact__item">
          <svg class="contact__icon" viewBox="0 0 12 12" aria-hidden="true"><path d="M4.5 7.5l3-3M3 6 1.5 7.5a2 2 0 0 0 3 3L6 9M9 6l1.5-1.5a2 2 0 0 0-3-3L6 3" fill="none" stroke="#7a1a10" stroke-width="1.5"/></svg>
          www.ironvale.com
        </li>
      </ul>
    </div>
  </section>

  <section class="card card--back" aria-label="Business card back">
    <div class="brand">
      <span class="brand__dot" aria-hidden="true"></span>
      <div class="brand__text">
        <p class="brand__name">IRONVALE</p>
        <p class="brand__tagline">SECURITY SYSTEMS INC.</p>
      </div>
    </div>
  </section>
</main>
</body>
</html>
```